Labels for Bees Wax Candles & Honey Jars

We need labels for jars of natural honey. Most of our jars are square and the labels about 2" by 2".

Also we make bees wax candles of various sizes. We wish to wrap th enables around the circular candles which are between 2" and 3" in diameter... thus another have inch per label so they can be attached adhesively. The candles also vary in height... therefor th enables need to be 1.5", 2" and 3" in height.

We ar elooking for a very artistic and simple label that may include vibrant colors.
The name of our company must be displayed.. Candles by Morrow and for the Honey.... Morrow's All Natural Honey
Updates

The labels will be used for both Honey Jars as well as Bees Wax candles. There will be various sizes but that is something that can be adjusted after the initial design is approved. The Honey Jars should read "Natural Honey by Morrow" and the Candle labels should read "Natural Bees Wax Candles by Morrow" I am interested in simple, colorful, legible, and arty labels that pertain to bees and the natural environment. Hope this helps. We may also use a similar design on our web page. The size of the label on the honey will be 2" by 2" and the candles will vary.

Target Market(s)

Individual that purchase natural and organic products.

Requirements
Must have
• Labels should be very creative but legible and the emphasis on the candles should be all natural bees wax and the emphasis on the honey should be all natural honey. We are talking about the same design but different sizes and names.
Nice to have
• brillant colors and artistic

```html
<!DOCTYPE html>
<html lang="en">
<head>
<meta charset="utf-8">
<title>Morrow's Honey &amp; Candle Labels</title>
<link rel="stylesheet" href="https://fonts.googleapis.com/css2?family=Italianno&family=Roboto+Condensed:wght@700&family=Crimson+Text:wght@700&display=swap">
<style>
  :root {
    --page: #ffffff;
    --amber: #f6a81b;
    --amber-soft: #f9c766;
    --cream: #fff6e2;
    --honey-cell: #f9d445;
    --honey-gap: #ffffff;
    --wax-cell: #1a1a1a;
    --wax-gap: #ffffff;
    --ink: #111111;
  }
  * { margin: 0; padding: 0; box-sizing: border-box; }
  html, body {
    width: 1200px; height: 1200px; overflow: hidden;
    background: var(--page);
  }
  .sheet { position: relative; width: 1200px; height: 1200px; }

  .label {
    position: absolute;
    width: 343px; height: 343px;
  }
  .label--candle { left: 425px; top: 228px; }
  .label--honey-sans { left: 205px; top: 642px; }
  .label--honey-serif { left: 631px; top: 642px; }

  .label__pattern {
    position: absolute; inset: 0;
  }
  .label--candle .label__pattern {
    background:
      linear-gradient(135deg, var(--wax-cell) 0%, #5a5a5a 50%, var(--wax-cell) 100%);
  }
  .label--honey-sans .label__pattern,
  .label--honey-serif .label__pattern {
    background:
      linear-gradient(135deg, var(--honey-cell) 0%, #fcebb0 50%, var(--honey-cell) 100%);
  }

  .label__panel {
    position: absolute; inset: 31px;
    background: var(--amber);
    border-radius: 10px;
  }

  .label__name {
    position: absolute; left: 0; right: 0; top: 8px;
    text-align: center;
    font-family: "Italianno", cursive;
    font-weight: 400;
    font-size: 80px; line-height: 1;
    color: var(--ink);
  }

  .label__art {
    position: absolute;
    left: 36px; top: 100px;
    width: 209px; height: 102px;
    border-radius: 12px;
    background: radial-gradient(ellipse at 50% 55%, var(--cream) 0%, var(--amber-soft) 60%, var(--amber) 100%);
  }

  .label__product {
    position: absolute; left: 0; right: 0;
    text-align: center; color: var(--ink);
    font-weight: 700;
  }
  .label--candle .label__product {
    top: 219px;
    font-family: "Crimson Text", serif;
    font-size: 22px; line-height: 1.15;
  }
  .label--honey-sans .label__product {
    top: 230px;
    font-family: "Roboto Condensed", sans-serif;
    font-size: 26px;
  }
  .label--honey-serif .label__product {
    top: 227px;
    font-family: "Crimson Text", serif;
    font-size: 29px;
  }
</style>
</head>
<body>
<main class="sheet">

  <section class="label label--candle">
    <div class="label__pattern" role="img" aria-label="Black and white honeycomb pattern border"></div>
    <div class="label__panel">
      <h2 class="label__name">Morrow's</h2>
      <div class="label__art" role="img" aria-label="Illustration of a white beehive with two bees flying on a dotted path"></div>
      <p class="label__product">Natural Bees Wax<br>Candles</p>
    </div>
  </section>

  <section class="label label--honey-sans">
    <div class="label__pattern" role="img" aria-label="Yellow and white honeycomb pattern border"></div>
    <div class="label__panel">
      <h2 class="label__name">Morrow's</h2>
      <div class="label__art" role="img" aria-label="Illustration of a white beehive with two bees flying on a dotted path"></div>
      <p class="label__product">All Natural Honey</p>
    </div>
  </section>

  <section class="label label--honey-serif">
    <div class="label__pattern" role="img" aria-label="Yellow and white honeycomb pattern border"></div>
    <div class="label__panel">
      <h2 class="label__name">Morrow's</h2>
      <div class="label__art" role="img" aria-label="Illustration of a white beehive with two bees flying on a dotted path"></div>
      <p class="label__product">All Natural Honey</p>
    </div>
  </section>

</main>
</body>
</html>
```